Business card design for an industrial flooring company

Designing a eco-friendly/go green/organic looking business card for a concrete Polishing / epoxy coatings company. I am looking for an ecofriendly / organic / go green feel for an industrial flooring company. I need a logo bad. We go out of are way to protect the area where we are working. Filter the air, dispose of the contaminated water, use low VOC products etc. We travel nationwide doing concrete polishing and epoxy coatings for big box stores like Halvane Pondery FurNook penny central. When someone googles environmentally friendly flooring solutions I want them to call me I’m really easy looking for something clean and professional.

Target Market(s)

We target industrial facilities managers all the way to small business owner. Anyone that has a concrete floor. Warehouses, retail space, shops, etc.

Industry/Entity Type

Construction Company

Contact Information for Business Card

Business name- Terra-Gleam, office 555-310-4829, cell 555-847-1906, email dwight@terra-gleam-example.com. No Address

Font styles to use
Serif
Sans Serif
Other font styles liked:
• Arial

Colors
3176b5
85acd3
cfdfed
cedeed
00a990
33b8a4

Requirements
Must have
• Environmentally friendly concrete polishing systems
• Services: Polished concrete, epoxy coatings, overlays, safety striping, staining and dyed concrete, concrete sealing
• a eco-friendly/go green/organic look
Nice to have
• I am looking for an ecofriendly / organic / go green feel for an industrial flooring company. I need a logo bad. We go out of are way to protect the area where we are working. Filter the air, dispose of the contaminated water, use low VOC products.
Should not have
• Shouldn’t be childish unprofessional
• I do not like the logo I attached.

```html
<!DOCTYPE html>
<html lang="en">
<head>
<meta charset="utf-8">
<title>Terra-Gleam Business Card</title>
<link href="https://fonts.googleapis.com/css2?family=Lato:wght@300;400;700&family=Roboto:wght@400;500;700&display=swap" rel="stylesheet">
<style>
  :root {
    --teal: #00a990;
    --teal-light: #33b8a4;
    --blue: #3176b5;
    --blue-soft: #85acd3;
    --blue-pale: #cfdfed;
    --ink: #2b2b2b;
    --white: #ffffff;
    --backdrop: #ece9e4;
    --icon: #4fa3b0;
  }
  * { margin: 0; padding: 0; box-sizing: border-box; }
  html, body { width: 900px; height: 1200px; overflow: hidden; }
  body { background: var(--backdrop); position: relative; font-family: "Roboto", Arial, sans-serif; }

  .card {
    position: absolute; left: 86px; width: 732px; height: 428px;
    border-radius: 28px; box-shadow: 0 6px 14px rgba(0,0,0,0.25);
  }
  .card-front { top: 131px; background: var(--white); }
  .card-back { top: 634px; background: var(--teal); }

  .person { position: absolute; left: 50px; top: 90px; font-family: "Lato", Arial, sans-serif; white-space: nowrap; }
  .person-name { font-size: 28px; line-height: 32px; letter-spacing: 0.2px; }
  .person-name .first { color: var(--teal); font-weight: 700; }
  .person-name .last { color: var(--blue); font-weight: 300; }
  .person-role { color: var(--teal); font-size: 16px; margin-top: 2px; }

  .brand { position: absolute; text-align: right; white-space: nowrap; }
  .brand-name {
    font-family: "Roboto", Arial, sans-serif; font-weight: 700;
    font-size: 54px; line-height: 60px; color: var(--teal); letter-spacing: -0.5px;
  }
  .brand-tagline {
    display: inline-block; background: var(--blue-soft); color: var(--white);
    font-size: 14px; line-height: 27px; padding: 0 13px; border-radius: 9px; margin-top: 6px;
  }
  .card-front .brand { right: 46px; top: 70px; }
  .card-back .brand { left: 0; right: 0; top: 166px; text-align: center; }
  .card-back .brand-name { color: var(--white); font-size: 60px; line-height: 64px; }

  .contacts { position: absolute; left: 50px; top: 248px; list-style: none; }
  .contacts li {
    display: flex; align-items: center; height: 28.5px;
    font-size: 17px; color: var(--ink);
  }
  .contacts svg { width: 22px; height: 22px; margin-right: 10px; flex: none; }

  .services { position: absolute; right: 46px; top: 222px; text-align: right; }
  .services h2 { color: var(--teal); font-size: 19px; font-weight: 500; margin-bottom: 5px; }
  .services ul { list-style: none; }
  .services li { font-size: 16.5px; line-height: 22.8px; color: var(--ink); }
  .services li::after {
    content: ""; display: inline-block; width: 7px; height: 7px; border-radius: 50%;
    background: var(--blue-soft); margin-left: 8px; vertical-align: middle;
  }
</style>
</head>
<body>

<section class="card card-front">
  <div class="person">
    <p class="person-name"><span class="first">DWIGHT</span> <span class="last">MARLOWE</span></p>
    <p class="person-role">Managing Director</p>
  </div>

  <div class="brand">
    <p class="brand-name">Terra-Gleam</p>
    <p class="brand-tagline">Environmentally Friendly Concrete Polishing Systems</p>
  </div>

  <ul class="contacts">
    <li>
      <svg viewBox="0 0 22 22" aria-hidden="true"><circle cx="11" cy="11" r="11" fill="var(--icon)"/><path d="M6 9 Q11 5 16 9 L15 10.5 L13 10 L13 9 Q11 8.2 9 9 L9 10 L7 10.5 Z M7.5 11.5 H14.5 L15.5 15.5 H6.5 Z" fill="#fff"/></svg>
      555-310-4829
    </li>
    <li>
      <svg viewBox="0 0 22 22" aria-hidden="true"><circle cx="11" cy="11" r="11" fill="var(--icon)"/><rect x="7.5" y="4.5" width="7" height="13" rx="1.2" fill="#fff"/><rect x="8.7" y="6" width="4.6" height="7" fill="var(--icon)"/></svg>
      555-847-1906
    </li>
    <li>
      <svg viewBox="0 0 22 22" aria-hidden="true"><circle cx="11" cy="11" r="11" fill="var(--icon)"/><rect x="5.5" y="7" width="11" height="8" fill="#fff"/><path d="M5.5 7 L11 11.5 L16.5 7" fill="none" stroke="var(--icon)" stroke-width="1"/></svg>
      dwight@terra-gleam-example.com
    </li>
    <li>
      <svg viewBox="0 0 22 22" aria-hidden="true"><circle cx="11" cy="11" r="11" fill="var(--icon)"/><g fill="none" stroke="#fff" stroke-width="1.1"><circle cx="11" cy="11" r="6"/><ellipse cx="11" cy="11" rx="2.6" ry="6"/><path d="M5 11 H17 M6 8 H16 M6 14 H16"/></g></svg>
      www.terra-gleam-example.com
    </li>
    <li>
      <svg viewBox="0 0 22 22" aria-hidden="true"><circle cx="11" cy="11" r="11" fill="var(--icon)"/></svg>
      1gleamfloors
    </li>
  </ul>

  <div class="services">
    <h2>Services</h2>
    <ul>
      <li>Polished Concrete</li>
      <li>Epoxy Coatings</li>
      <li>Overlays</li>
      <li>Safety Striping</li>
      <li>Staining and Dyed Concrete</li>
      <li>Concrete Sealing</li>
    </ul>
  </div>
</section>

<section class="card card-back">
  <div class="brand">
    <p class="brand-name">Terra-Gleam</p>
    <p class="brand-tagline">Environmentally Friendly Concrete Polishing Systems</p>
  </div>
</section>

</body>
</html>
```